Tidal Pastry Depot Business card

We are empanada whole-sellers and I want a business card design with a picture of an empanada on it that also mentions first trial order FREE. our contact number 555-274-1193 our website www.zarifaban.com and business email Tomas@zarifaban.com

If you want any of our artwork please feel free to email me at the address above.

```html
<!DOCTYPE html>
<html lang="en">
<head>
<meta charset="utf-8">
<title>Tidal Pastry Depot – Business Card</title>
<link rel="stylesheet" href="https://fonts.googleapis.com/css2?family=Alfa+Slab+One&family=Archivo+Black&family=Roboto:wght@400;500&display=swap">
<style>
  :root {
    --page-bg: #f1f1f1;
    --card-yellow: #f5b81c;
    --card-yellow-light: #f8c63a;
    --card-yellow-deep: #e9a60f;
    --ink: #1a1712;
    --band: #1c1a16;
    --band-text: #f7c531;
    --pastry-light: #f4d79c;
    --pastry-dark: #c98a3c;
    --pile-light: #f7d65a;
    --pile-dark: #d9a516;
  }
  * { box-sizing: border-box; margin: 0; padding: 0; }
  html, body { width: 1200px; height: 900px; overflow: hidden; }
  body {
    background: var(--page-bg);
    position: relative;
    font-family: "Roboto", sans-serif;
  }
  .card {
    position: absolute;
    top: 295px;
    width: 540px;
    height: 310px;
    border-radius: 24px;
    background: var(--card-yellow);
    overflow: hidden;
    box-shadow: 0 10px 24px rgba(0,0,0,0.12);
  }
  .card--front { left: 40px; }
  .card--back { left: 620px; }

  .card-pattern {
    position: absolute;
    inset: 0;
    background: linear-gradient(160deg, var(--card-yellow-light) 0%, var(--card-yellow) 50%, var(--card-yellow-deep) 100%);
  }

  .flower {
    position: absolute;
    width: 58px;
    height: 58px;
    border-radius: 50%;
    background: var(--ink);
  }
  .card--front .flower--top { left: 4px; top: 8px; }
  .card--front .flower--bottom { left: 468px; top: 236px; }
  .card--back .flower--top { left: 8px; top: 6px; }
  .card--back .flower--bottom { left: 470px; top: 214px; }

  .brand {
    position: absolute;
    left: 0;
    right: 0;
    text-align: center;
    color: var(--ink);
  }
  .brand__name {
    font-family: "Alfa Slab One", serif;
    font-size: 38px;
    line-height: 1;
    white-space: nowrap;
  }
  .brand__tagline {
    font-family: "Alfa Slab One", serif;
    font-size: 17px;
    letter-spacing: 0.5px;
    margin-top: 16px;
    white-space: nowrap;
  }
  .card--front .brand { top: 62px; padding-left: 30px; }
  .card--back .brand { top: 58px; padding-left: 50px; padding-right: 10px; }
  .card--back .brand__name { font-size: 36px; }
  .card--back .brand__tagline { font-size: 15px; margin-top: 14px; }

  .contact-band {
    position: absolute;
    left: 0;
    top: 190px;
    width: 470px;
    height: 82px;
    background: var(--band);
    padding: 9px 0 0 26px;
  }
  .contact-band ul { list-style: none; }
  .contact-band li {
    display: flex;
    align-items: center;
    gap: 8px;
    color: var(--band-text);
    font-size: 17px;
    line-height: 22px;
  }
  .contact-band svg { width: 17px; height: 17px; fill: var(--band-text); }

  .pastry-photo {
    position: absolute;
    left: 262px;
    top: 180px;
    width: 200px;
    height: 110px;
    border-radius: 50px 50px 40px 60px;
    background: radial-gradient(ellipse at 40% 45%, var(--pastry-light), var(--pastry-dark));
  }

  .pastry-pile {
    position: absolute;
    inset: 0;
    background: radial-gradient(ellipse at 45% 55%, var(--pile-light) 0%, var(--card-yellow) 55%, var(--pile-dark) 100%);
  }

  .offer {
    position: absolute;
    left: 140px;
    top: 180px;
    width: 280px;
    text-align: center;
    font-family: "Archivo Black", sans-serif;
    color: var(--ink);
    font-size: 20px;
    line-height: 28px;
  }
</style>
</head>
<body>
  <section class="card card--front">
    <div class="card-pattern" role="img" aria-label="Yellow geometric tile pattern"></div>
    <div class="flower flower--top" role="img" aria-label="Black flower ornament"></div>
    <div class="brand">
      <div class="brand__name">Tidal Pastry Depot</div>
      <div class="brand__tagline">MALAYSIAN &amp; THAI STREET FOOD</div>
    </div>
    <div class="contact-band">
      <ul>
        <li>
          <svg viewBox="0 0 24 24"><path d="M6.6 10.8a15.1 15.1 0 0 0 6.6 6.6l2.2-2.2a1 1 0 0 1 1-.25 11.4 11.4 0 0 0 3.6.57 1 1 0 0 1 1 1V20a1 1 0 0 1-1 1A17 17 0 0 1 3 4a1 1 0 0 1 1-1h3.5a1 1 0 0 1 1 1c0 1.25.2 2.45.57 3.57a1 1 0 0 1-.25 1z"/></svg>
          555-274-1193
        </li>
        <li>
          <svg viewBox="0 0 24 24"><path d="M12 2a10 10 0 1 0 0 20 10 10 0 0 0 0-20zm6.9 6h-2.9a15.7 15.7 0 0 0-1.4-3.6A8 8 0 0 1 18.9 8zM12 4c.8 1.2 1.5 2.5 1.9 4h-3.8c.4-1.5 1.1-2.8 1.9-4zM4.3 14a8 8 0 0 1 0-4h3.4a16 16 0 0 0 0 4zm.8 2h2.9c.3 1.300.8 2.5 1.4 3.6A8 8 0 0 1 5.1 16zM8 8H5.1a8 8 0 0 1 4.3-3.6C8.8 5.5 8.4 6.7 8 8zm4 12c-.8-1.2-1.5-2.5-1.9-4h3.8c-.4 1.5-1.1 2.8-1.9 4zm2.3-6H9.7a14.7 14.7 0 0 1 0-4h4.6a14.7 14.7 0 0 1 0 4zm.3 5.6c.6-1.1 1.1-2.3 1.4-3.6h2.9a8 8 0 0 1-4.3 3.6zm1.7-5.6a16 16 0 0 0 0-4h3.4a8 8 0 0 1 0 4z"/></svg>
          www.zarifaban.com
        </li>
        <li>
          <svg viewBox="0 0 24 24"><path d="M3 5h18a1 1 0 0 1 1 1v12a1 1 0 0 1-1 1H3a1 1 0 0 1-1-1V6a1 1 0 0 1 1-1zm1 2.2V17h16V7.2l-8 5.3z"/></svg>
          Tomas@zarifaban.com
        </li>
      </ul>
    </div>
    <div class="pastry-photo" role="img" aria-label="Photo of golden empanadas, one cut open to show the filling"></div>
    <div class="flower flower--bottom" role="img" aria-label="Black flower ornament"></div>
  </section>

  <section class="card card--back">
    <div class="pastry-pile" role="img" aria-label="Yellow-toned photo of rows of crimped empanadas over a tile pattern"></div>
    <div class="flower flower--top" role="img" aria-label="Black flower ornament"></div>
    <div class="brand">
      <div class="brand__name">Tidal Pastry Depot</div>
      <div class="brand__tagline">MALAYSIAN &amp; THAI STREET FOOD</div>
    </div>
    <p class="offer">first trial order<br>FREE</p>
    <div class="flower flower--bottom" role="img" aria-label="Black flower ornament"></div>
  </section>
</body>
</html>
```